Business Card Design for Brightkeel

The company provides engineering tender consulting services and personnel resources. The target market is large engineering construction and services companies. The business is based in Australia.

```html
<!DOCTYPE html>
<html lang="en">
<head>
<meta charset="utf-8">
<title>Brightkeel Business Card</title>
<link rel="stylesheet" href="https://fonts.googleapis.com/css2?family=PT+Sans+Narrow:wght@400&display=swap">
<style>
  :root {
    --page: #ffffff;
    --card: #ffffff;
    --card-edge: #c9c9c9;
    --ink: #1c1c1c;
    --brand-dot: #2a9fd6;
    --green: #6cbd45;
    --teal: #1f9a8a;
    --blue: #2f56a8;
    --pink: #ec4f9b;
    --yellow: #f5d21c;
    --sky: #7fc7ea;
  }
  * { margin: 0; padding: 0; box-sizing: border-box; }
  html, body { width: 958px; height: 1200px; overflow: hidden; background: var(--page); }
  body { position: relative; font-family: "PT Sans Narrow", "Arial Narrow", sans-serif; color: var(--ink); }

  .card {
    position: absolute;
    left: 29px;
    width: 924px;
    background: var(--card);
    border: 2px solid var(--card-edge);
    overflow: hidden;
  }
  .card--back { top: 30px; height: 548px; }
  .card--front { top: 615px; height: 555px; }

  .pattern-area { position: absolute; left: 0; right: 0; }
  .pattern-area--faint {
    top: 130px;
    height: 310px;
    opacity: 0.22;
    background: linear-gradient(90deg, var(--green), var(--sky) 35%, var(--pink) 62%, var(--sky));
  }
  .pattern-area--bold {
    top: 300px;
    height: 215px;
    opacity: 0.75;
    background: linear-gradient(90deg, var(--green), var(--teal) 20%, var(--blue) 35%, var(--yellow) 45%, var(--pink) 58%, var(--teal) 78%, var(--green));
  }

  .person { position: absolute; left: 140px; top: 205px; }
  .person__name { font-size: 28px; line-height: 1.2; }
  .person__role, .person__phone { font-size: 23px; line-height: 1.45; }

  .contact { position: absolute; left: 657px; top: 92px; }
  .contact__company { font-size: 40px; line-height: 1.2; margin-bottom: 6px; }
  .contact__line { font-size: 25px; line-height: 1.62; white-space: nowrap; }

  .brand {
    position: absolute;
    left: 320px;
    top: 192px;
    display: flex;
    align-items: center;
    gap: 20px;
  }
  .brand__dot { width: 64px; height: 64px; border-radius: 50%; background: var(--brand-dot); }
  .brand__name { font-size: 40px; line-height: 1; }
</style>
</head>
<body>

<section class="card card--back">
  <div class="pattern-area pattern-area--faint" role="img" aria-label="Faint decorative wave of multicoloured mosaic tiles sweeping across the card"></div>

  <div class="person">
    <p class="person__name">Marcus Ellery</p>
    <p class="person__role">Deputy Manager</p>
    <p class="person__phone">+91 8812340567</p>
  </div>

  <div class="contact">
    <p class="contact__company">Brightkeel</p>
    <p class="contact__line">M: 9999 999 999</p>
    <p class="contact__line">T:&nbsp;&nbsp; 99 9999 9999</p>
    <p class="contact__line">E: nnnn@nnn.com.au</p>
    <p class="contact__line">PO Box 99</p>
    <p class="contact__line">Nnnnnnnnn, Nnn,</p>
    <p class="contact__line">9999</p>
    <p class="contact__line">ABN99999999999</p>
  </div>
</section>

<section class="card card--front">
  <div class="pattern-area pattern-area--bold" role="img" aria-label="Bold decorative wave of mosaic tiles in green, teal, blue, yellow and pink crossing the card"></div>

  <div class="brand">
    <span class="brand__dot"></span>
    <span class="brand__name">Brightkeel</span>
  </div>
</section>

</body>
</html>
```